Stationery Design Project

We need letterhead and business cards designed for our consulting firm. Color scheme, mostly deep blue (see logo). We are a commercial consulting work out firm, nationwide (large loans, $10MM and up). Visit our website for more info.
Updates

Project Deadline Extended
Reason: Meeting tomorrow morning to make final final decision. Would like this project to stay open to be able to provide feed back and receive final edits and approve. Thank you!!!

Target Market(s)

High end investors

Industry/Entity Type

Business

Requirements
Must have
• Letterhead must have the logo and the address

4719 Harlow Court, Suite 210, San Diego, CA 92108
Nice to have
• It would be nice to incorporate a watermark of all or some portion of the logo on the letterhead, or at least for the 2nd sheets.

Maybe our phone number: 858.555.0172
and/or webiste: www.tallpinecapital-example.com
Should not have
• Target users and audience of this will be men so, frilly or whimsical type designs are not preferred.

```html
<!DOCTYPE html>
<html lang="en">
<head>
<meta charset="utf-8">
<title>Tallpine Capital Stationery</title>
<link href="https://fonts.googleapis.com/css2?family=Roboto:wght@300;400;500&display=swap" rel="stylesheet">
<style>
  :root {
    --backdrop: #96a1a6;
    --paper: #ffffff;
    --ink: #5b6268;
    --brand-grey: #5f6b72;
    --brand-blue: #2a86dc;
    --link-blue: #5fa9e6;
    --rule: #7d878c;
    --shadow: rgba(40, 48, 52, 0.55);
  }
  * { margin: 0; padding: 0; box-sizing: border-box; }
  html, body { width: 1200px; height: 900px; overflow: hidden; }
  body {
    position: relative;
    background: var(--backdrop);
    font-family: "Roboto", Helvetica, Arial, sans-serif;
    font-weight: 300;
    color: var(--ink);
  }
  .sheet {
    position: absolute;
    background: var(--paper);
    box-shadow: 6px 6px 8px var(--shadow);
  }
  .letterhead { left: 58px; top: 32px; width: 588px; height: 832px; }
  .envelope { left: 527px; top: 468px; width: 617px; height: 311px; }
  .card { width: 253px; height: 155px; border-radius: 14px; }
  .card-front { left: 690px; top: 75px; }
  .card-back { left: 884px; top: 255px; }

  .brand {
    position: absolute;
    display: flex;
    align-items: center;
    gap: 6px;
    color: var(--brand-grey);
    font-weight: 400;
    white-space: nowrap;
  }
  .brand-mark { background: var(--brand-blue); flex: none; }

  .letterhead .brand { left: 28px; top: 80px; font-size: 17px; }
  .letterhead .brand-mark { width: 12px; height: 12px; }
  .card-front .brand { left: 0; right: 0; justify-content: center; top: 68px; font-size: 19px; }
  .card-front .brand-mark { width: 13px; height: 13px; }
  .envelope .brand { left: 29px; top: 62px; font-size: 17px; }
  .envelope .brand-mark { width: 12px; height: 12px; }
  .card-back .brand { right: 16px; top: 118px; font-size: 11px; gap: 4px; }
  .card-back .brand-mark { width: 8px; height: 8px; }

  .contact { position: absolute; font-size: 8px; line-height: 10px; }
  .contact p + p { margin-top: 5px; }
  .letterhead .contact { left: 28px; top: 747px; }
  .envelope .contact { left: 28px; top: 230px; }

  .footer-rule { position: absolute; height: 1px; background: var(--rule); }
  .letterhead .footer-rule { left: 28px; top: 797px; width: 432px; }
  .envelope .footer-rule { left: 28px; top: 279px; width: 456px; }
  .card-back .footer-rule { left: 17px; top: 81px; width: 124px; }

  .web { position: absolute; font-size: 8px; color: var(--link-blue); white-space: nowrap; }
  .letterhead .web { right: 26px; top: 792px; }
  .envelope .web { right: 27px; top: 274px; }
  .card-back .web { right: 16px; top: 76px; font-size: 7.5px; }

  .person { position: absolute; left: 17px; top: 16px; font-size: 8px; line-height: 10px; }
  .person-name { color: var(--brand-blue); font-weight: 500; font-size: 8.5px; }
  .card-lines { position: absolute; right: 16px; top: 16px; text-align: right; font-size: 7.5px; line-height: 9.5px; }
  .card-back .contact { left: 17px; top: 120px; font-size: 7.5px; line-height: 9.5px; }
</style>
</head>
<body>

<section class="sheet letterhead" aria-label="Letterhead">
  <div class="brand"><span class="brand-mark"></span>Tallpine Capital</div>
  <div class="contact">
    <p>4719 Harlow Court, Suite 210<br>San Diego, CA 92108</p>
    <p>tel: 858 555 0172<br>info@tallpinecapital-example.com</p>
  </div>
  <div class="footer-rule"></div>
  <div class="web">www.tallpinecapital-example.com</div>
</section>

<section class="sheet card card-front" aria-label="Business card front">
  <div class="brand"><span class="brand-mark"></span>Tallpine Capital</div>
</section>

<section class="sheet card card-back" aria-label="Business card back">
  <div class="person">
    <div class="person-name">Daniel Reyes</div>
    <div>Chief Executive Officer</div>
  </div>
  <div class="card-lines">
    tel: 858 555 0172<br>
    fax: 858 555 0184<br>
    cell: 858 555 0139<br>
    e-mail: info@tallpinecapital-example.com
  </div>
  <div class="footer-rule"></div>
  <div class="web">www.tallpinecapital-example.com</div>
  <div class="contact">
    <p>4719 Harlow Court, Suite 210<br>San Diego, CA 92108</p>
  </div>
  <div class="brand"><span class="brand-mark"></span>Tallpine Capital</div>
</section>

<section class="sheet envelope" aria-label="Envelope">
  <div class="brand"><span class="brand-mark"></span>Tallpine Capital</div>
  <div class="contact">
    <p>4719 Harlow Court, Suite 210<br>San Diego, CA 92108</p>
    <p>tel: 858 555 0172<br>info@tallpinecapital-example.com</p>
  </div>
  <div class="footer-rule"></div>
  <div class="web">www.tallpinecapital-example.com</div>
</section>

</body>
</html>
```